Enhance Landing Page

Actual: https://thecoralparlor.com/aposte-em-solaria-lp-port/

I need a better design for this page:
Using this shortcodes : https://sturdy.qvxlayouts.net
Rules:
. Keep the page header
. Keep the footer

```html
<!DOCTYPE html>
<html lang="pt-BR">
<head>
<meta charset="utf-8">
<title>Coral Parlor – Invista na Florida</title>
<link href="https://fonts.googleapis.com/css2?family=Montserrat:wght@400;600;700;800&family=Open+Sans:wght@400;600&display=swap" rel="stylesheet">
<style>
:root{
  --pink:#e2197b;
  --purple:#5a2a86;
  --purple-dark:#3f1c63;
  --orange:#f7931e;
  --green:#3fb24a;
  --teal:#22b6c3;
  --dark:#262626;
  --ink:#444;
  --muted:#888;
  --light:#f4f4f4;
  --white:#fff;
}
*{box-sizing:border-box;margin:0;padding:0}
html,body{width:1200px;height:4224px;overflow:hidden}
body{font-family:"Open Sans",Arial,sans-serif;color:var(--ink);background:var(--white);position:relative}
h1,h2,h3,h4,.brand,.btn{font-family:"Montserrat",Arial,sans-serif}
.abs{position:absolute}
.img{position:absolute}
.btn{display:inline-block;border-radius:20px;padding:9px 26px;font-size:13px;font-weight:700;color:#fff}
.btn-orange{background:var(--orange)}
.btn-purple{background:var(--purple)}

/* header */
.site-header{position:absolute;top:0;left:0;width:1200px;height:58px;background:#fff;box-shadow:0 2px 6px rgba(0,0,0,.08);z-index:5}
.phone-pill{position:absolute;top:10px;height:18px;border-radius:9px;background:var(--green);color:#fff;font-size:10px;font-weight:600;padding:2px 10px}
.header-note{position:absolute;top:32px;font-size:9px;color:var(--muted)}
.brand{position:absolute;left:530px;top:12px;display:flex;align-items:center;gap:8px;font-weight:800;color:var(--pink);font-size:20px;letter-spacing:1px}
.brand .dot{width:14px;height:14px;border-radius:50%;background:var(--pink)}
.header-cta{position:absolute;top:12px;display:flex;align-items:center;gap:6px;font-size:9px;color:var(--muted);line-height:1.2}
.header-cta i{width:26px;height:26px;border-radius:50%;display:block}

/* hero */
.hero{position:absolute;top:58px;left:0;width:1200px;height:582px;overflow:hidden}
.hero-bg{left:0;top:0;width:1200px;height:582px;background:linear-gradient(180deg,#8fb27c 0%,#cfe0b5 45%,#7aa25d 100%)}
.hero-people{left:600px;top:40px;width:400px;height:542px;border-radius:200px 200px 0 0;background:linear-gradient(160deg,#d9b59a,#8a6a56)}
.hero-title{position:absolute;left:186px;top:36px;width:290px;height:290px;border-radius:50%;background:var(--pink);color:#fff;display:flex;flex-direction:column;justify-content:center;padding-left:34px}
.hero-title h1{font-size:30px;line-height:1.18;font-weight:700}
.hero-title h1 b{font-weight:800;color:#ffd9ea}
.hero-sub{position:absolute;left:456px;top:270px;width:200px;height:200px;border-radius:50%;background:var(--purple);color:#fff;display:flex;align-items:center;padding:0 30px;font-size:15px;line-height:1.35}

/* intro */
.intro{position:absolute;top:640px;left:0;width:1200px;height:440px;background:#fff}
.intro-photo-left{left:-140px;top:60px;width:360px;height:360px;border-radius:50%;background:linear-gradient(135deg,#c8d9e6,#7e8f9b)}
.intro-text{position:absolute;left:244px;top:44px;width:340px}
.intro-text h2{font-size:20px;font-weight:700;color:var(--dark);margin-bottom:14px}
.intro-text h2 em{font-style:normal;color:var(--pink)}
.intro-text p{font-size:11px;line-height:1.6;color:var(--muted);margin-bottom:10px}
.intro-text .btn{margin-top:6px;padding:7px 18px;font-size:11px}
.contact-circle{position:absolute;left:632px;top:30px;width:330px;height:330px;border-radius:50%;background:var(--orange);padding:60px 64px 0;color:#fff}
.contact-circle h3{font-size:20px;text-align:center;margin-bottom:16px}
.field{height:26px;border-radius:13px;background:rgba(255,255,255,.85);margin-bottom:10px;font-size:10px;color:var(--muted);padding:6px 14px}
.contact-circle .btn{display:block;width:100px;margin:6px auto 0;background:var(--purple);padding:6px 0;text-align:center;font-size:11px}
.intro-photo-right{left:900px;top:-10px;width:400px;height:400px;border-radius:50%;background:linear-gradient(160deg,#9fc7de,#e5d6c3 60%,#7a6a5a);border:6px solid #fff}

/* services */
.services{position:absolute;top:1080px;left:0;width:1200px;height:360px}
.service-grid{position:absolute;left:260px;top:40px;width:680px;display:grid;grid-template-columns:repeat(4,1fr);row-gap:36px}
.service{text-align:center;font-size:11px;color:var(--muted)}
.service .ring{width:92px;height:92px;border-radius:50%;border:2px solid #e5e5e5;margin:0 auto 10px;display:flex;align-items:center;justify-content:center}
.service svg{width:38px;height:38px;stroke:var(--orange);fill:none;stroke-width:2.2;stroke-linecap:round;stroke-linejoin:round}
.branch{background:linear-gradient(90deg,rgba(140,100,70,.0),rgba(140,100,70,.35),rgba(232,138,90,.4));border-radius:40px}

/* vision */
.vision{position:absolute;top:1440px;left:0;width:1200px;height:450px}
.vision svg.band{position:absolute;left:0;top:0}
.vision-text{position:absolute;left:240px;top:112px;width:360px;color:#fff}
.vision-text h2{font-size:30px;font-weight:800;margin-bottom:12px}
.vision-text h4{font-size:13px;font-weight:600;margin-bottom:14px;line-height:1.4}
.vision-text p{font-size:11px;line-height:1.6;opacity:.85;margin-bottom:16px}
.vision-divider{position:absolute;left:620px;top:120px;width:1px;height:220px;background:rgba(255,255,255,.35)}
.vision-cta{position:absolute;left:660px;top:160px;width:260px;text-align:center;color:#fff}
.vision-cta h3{font-size:22px;line-height:1.3;margin-bottom:18px}
.vision-cta .btn{font-size:11px;padding:7px 20px}

/* gallery */
.gallery{position:absolute;top:1905px;left:0;width:1200px;height:560px;display:grid;grid-template-columns:390px 390px 390px;grid-template-rows:265px 265px;gap:15px}
.gallery div{width:100%;height:100%}
.g1{background:linear-gradient(150deg,#d8dde0,#6d7a80)}
.g2{background:linear-gradient(150deg,#7b5c45,#2c241d)}
.g3{background:linear-gradient(180deg,#6fa3d8,#cfe3f0 55%,#6f8a4e)}
.g4{background:linear-gradient(180deg,#f1a560,#7a5890 55%,#4b5c36)}
.g5{background:linear-gradient(150deg,#c79a6a,#3b2a22)}
.g6{background:linear-gradient(180deg,#9fb8c8,#6f8f5a)}
.gallery-more{position:absolute;top:2484px;left:560px;font-size:11px;padding:6px 22px}

/* prices */
.prices{position:absolute;top:2560px;left:0;width:1200px;height:390px;overflow:hidden}
.prices-bg{left:0;top:0;width:1200px;height:390px;background:linear-gradient(180deg,#fff 0%,#eef0f1 40%,#dcdfe1 100%)}
.prices-house{left:150px;top:40px;width:330px;height:320px;border-radius:12px;background:radial-gradient(ellipse at 50% 45%,#c88450,#9a5a36 45%,rgba(230,200,180,0) 72%)}
.prices-text{position:absolute;left:720px;top:90px;width:320px}
.prices-text h2{font-size:22px;font-weight:600;color:var(--dark);line-height:1.3;margin-bottom:14px}
.prices-text p{font-size:11px;color:var(--muted);line-height:1.6;margin-bottom:16px}
.prices-text .btn{font-size:11px;padding:7px 20px}

/* builder */
.builder{position:absolute;top:2950px;left:0;width:1200px;height:500px;overflow:hidden}
.builder-bedroom{left:-60px;top:40px;width:400px;height:380px;border-radius:0 200px 200px 0;background:linear-gradient(160deg,#6b6b6b,#2d2d2d 60%,#bfb7a9)}
.builder-about{position:absolute;left:250px;top:60px;width:310px;height:310px;border-radius:50%;background:var(--purple);color:#fff;padding:64px 52px 0}
.builder-about h3{font-size:18px;margin-bottom:12px}
.builder-about p{font-size:11px;line-height:1.55;opacity:.9}
.stat{position:absolute;width:124px;height:124px;border-radius:50%;background:#fff;box-shadow:0 3px 12px rgba(0,0,0,.15);display:flex;flex-direction:column;align-items:center;justify-content:center;text-align:center;font-family:"Montserrat",sans-serif;color:var(--dark)}
.stat b{font-size:28px;font-weight:800;line-height:1}
.stat span{font-size:10px;letter-spacing:1px;margin-top:4px;text-transform:uppercase}
.builder-photo{left:880px;top:20px;width:420px;height:470px;border-radius:210px 0 0 210px;background:linear-gradient(170deg,#e8e2d4,#8b7a5a 55%,#3c5a34)}

/* lead form */
.lead{position:absolute;top:3450px;left:0;width:1200px;height:450px;background:linear-gradient(180deg,#fff,#f0f0f0)}
.lead-circle{position:absolute;left:430px;top:20px;width:400px;height:400px;border-radius:50%;background:#262626;color:#fff;text-align:center;padding-top:74px}
.lead-circle small{font-size:10px;color:#aaa}
.lead-circle h2{font-size:24px;margin:4px 0 14px}
.lead-circle p{font-size:10px;color:#aaa;margin-bottom:18px}
.lead-row{display:flex;gap:10px;width:260px;margin:0 auto 10px}
.lead-row .f{flex:1;height:24px;border:1px solid #555;font-size:9px;color:#888;text-align:left;padding:5px 8px}
.lead-area{width:260px;height:52px;margin:0 auto 14px;border:1px solid #555;font-size:9px;color:#888;text-align:left;padding:5px 8px}
.lead-circle .btn{font-size:11px;padding:5px 20px}
.skyline{left:0;top:400px;width:1200px;height:50px;background:linear-gradient(180deg,rgba(200,200,200,0),#e2e2e2)}

/* footer */
.site-footer{position:absolute;top:3900px;left:0;width:1200px;height:324px;background:#fff;border-top:1px solid #eee}
.footer-col{position:absolute;font-size:10px;color:var(--muted);line-height:1.6}
.footer-col h5{font-family:"Montserrat",sans-serif;font-size:11px;color:var(--dark);margin-top:6px}
.footer-col .pin{display:inline-block;width:8px;height:8px;border-radius:50%;background:var(--pink);margin-right:6px}
.footer-brand{position:absolute;left:510px;top:120px;display:flex;align-items:center;gap:8px;font-family:"Montserrat",sans-serif;font-weight:800;font-size:22px;color:var(--pink);letter-spacing:1px}
.footer-brand .dot{width:16px;height:16px;border-radius:50%;background:var(--pink)}
.footer-contacts{position:absolute;left:800px;top:40px;width:220px}
.footer-contacts .phone-pill{position:static;display:inline-block;margin-right:6px}
.footer-links{display:flex;gap:16px;margin-top:40px;font-size:9px;color:var(--muted)}
.footer-links span{display:flex;align-items:center;gap:6px}
.footer-links i{width:22px;height:22px;border-radius:50%;display:block}
.footer-bar{position:absolute;left:0;bottom:0;width:1200px;height:40px;background:#222;color:#aaa;font-size:9px;padding:14px 240px;display:flex;justify-content:space-between}
.footer-bar nav{display:flex;gap:24px;color:#ddd}
</style>
</head>
<body>

<header class="site-header">
  <span class="phone-pill" style="left:250px">(11) 4000-0000</span>
  <span class="header-note" style="left:250px">Atendimento Brasil</span>
  <span class="phone-pill" style="left:350px;background:#fff;color:var(--muted);padding:2px 0">(407) 555-0100</span>
  <span class="header-note" style="left:350px">Atendimento EUA</span>
  <div class="brand"><span class="dot"></span>CORAL PARLOR</div>
  <div class="header-cta" style="left:810px"><i style="background:var(--pink)"></i>Fale com<br>um Especialista</div>
  <div class="header-cta" style="left:890px"><i style="background:var(--teal)"></i>Agende sua<br>Consultoria</div>
</header>

<section class="hero">
  <div class="img hero-bg" role="img" aria-label="Parque ensolarado com árvores e gramado"></div>
  <div class="img hero-people" role="img" aria-label="Família sorrindo abraçada ao ar livre"></div>
  <div class="hero-title"><h1>Invista na <b>Florida</b><br>e Rentabilize<br>Tranquilidade</h1></div>
  <div class="hero-sub">Conheça as melhores oportunidades de investimentos na florida</div>
</section>

<section class="intro">
  <div class="img intro-photo-left" role="img" aria-label="Casa moderna com área externa"></div>
  <div class="intro-text">
    <h2>Presentes no <em>Brasil e Estados Unidos</em></h2>
    <p>A Coral Parlor é especializada em investimentos imobiliários na Florida, com equipes próprias em São Paulo e Orlando, oferecendo suporte completo do início ao fim.</p>
    <p>Nossa consultoria acompanha cada etapa: escolha do imóvel, financiamento, documentação, mobília e administração do aluguel, garantindo segurança e rentabilidade ao investidor.</p>
    <span class="btn btn-purple">Saiba Mais</span>
  </div>
  <div class="contact-circle">
    <h3>Fale Conosco</h3>
    <div class="field">Nome</div>
    <div class="field">E-mail</div>
    <div class="field">Telefone</div>
    <div class="field">Mensagem</div>
    <span class="btn">Enviar</span>
  </div>
  <div class="img intro-photo-right" role="img" aria-label="Sala de estar com vista para piscina"></div>
</section>

<section class="services">
  <div class="img branch" style="left:-20px;top:180px;width:200px;height:60px" role="img" aria-label="Galho florido decorativo"></div>
  <div class="img branch" style="left:1000px;top:60px;width:220px;height:60px;transform:scaleX(-1)" role="img" aria-label="Galho florido decorativo"></div>
  <div class="service-grid">
    <div class="service"><div class="ring"><svg viewBox="0 0 40 40"><rect x="6" y="12" width="28" height="16" rx="2"/><circle cx="20" cy="20" r="4"/></svg></div>Financiamento</div>
    <div class="service"><div class="ring"><svg viewBox="0 0 40 40"><path d="M26 12c-2-2-10-3-10 3s12 3 12 9-9 5-11 2M20 6v28"/></svg></div>Rentabilidade Garantida</div>
    <div class="service"><div class="ring"><svg viewBox="0 0 40 40"><rect x="12" y="5" width="16" height="30" rx="3"/><path d="M18 30h4"/></svg></div>Móveis</div>
    <div class="service"><div class="ring"><svg viewBox="0 0 40 40"><rect x="7" y="10" width="26" height="20" rx="2"/><path d="M7 16h26M12 25h6"/></svg></div>SSN e Crédito</div>
    <div class="service"><div class="ring"><svg viewBox="0 0 40 40"><rect x="10" y="5" width="20" height="30" rx="2"/><path d="M14 10h12M14 17h3M20 17h3M14 23h3M20 23h3M14 29h3M20 29h3"/></svg></div>Contabilidade</div>
    <div class="service"><div class="ring"><svg viewBox="0 0 40 40"><path d="M10 6h14l6 6v22H10z"/><path d="M15 16h10M15 22h10M15 28h6"/></svg></div>Documentação</div>
    <div class="service"><div class="ring"><svg viewBox="0 0 40 40"><circle cx="20" cy="13" r="6"/><path d="M9 34c0-7 5-11 11-11s11 4 11 11"/></svg></div>Mobília</div>
    <div class="service"><div class="ring"><svg viewBox="0 0 40 40"><path d="M6 20 20 8l14 12M10 17v17h20V17M17 34v-9h6v9"/></svg></div>Administração Da Casa</div>
  </div>
</section>

<section class="vision">
  <svg class="band" width="1200" height="450" viewBox="0 0 1200 450" aria-hidden="true">
    <path d="M0 40 Q300 0 600 30 T1200 20 V420 Q900 450 600 420 T0 430Z" fill="#5a2a86"/>
  </svg>
  <div class="vision-text">
    <h2>VISÃO 360°</h2>
    <h4>O sistema de atendimento mais seguro e completo do mercado na Florida.</h4>
    <p>Do primeiro contato à entrega das chaves, nossa equipe cuida de tudo: seleção do imóvel, análise de retorno, compra, decoração e gestão da locação, com relatórios mensais e total transparência para você investir com tranquilidade.</p>
    <span class="btn btn-orange">Saiba Mais Agora</span>
  </div>
  <div class="vision-divider"></div>
  <div class="vision-cta">
    <h3>Deseja Falar Com um Especialista?</h3>
    <span class="btn btn-orange">Agende Agora</span>
  </div>
</section>

<section class="gallery">
  <div class="g1" role="img" aria-label="Área de piscina coberta com mobiliário"></div>
  <div class="g2" role="img" aria-label="Cozinha planejada com ilha central"></div>
  <div class="g3" role="img" aria-label="Portal de entrada do condomínio Palm Crest"></div>
  <div class="g4" role="img" aria-label="Casa ao entardecer com jardim"></div>
  <div class="g5" role="img" aria-label="Salão de jogos com mesas"></div>
  <div class="g6" role="img" aria-label="Vista aérea de resort com piscinas"></div>
</section>
<span class="btn btn-purple gallery-more">Ver Mais</span>

<section class="prices">
  <div class="img prices-bg" role="img" aria-label="Fundo claro com mão segurando uma casa"></div>
  <div class="img prices-house" role="img" aria-label="Miniatura de casa sobre a palma da mão"></div>
  <div class="prices-text">
    <h2>Receba Preços e Plantas<br>Dos Imoveis</h2>
    <p>Cadastre-se e receba os valores, plantas e condições de pagamento dos imóveis disponíveis.</p>
    <span class="btn btn-orange">Solicitar</span>
  </div>
</section>

<section class="builder">
  <div class="img builder-bedroom" role="img" aria-label="Quarto decorado em tons escuros"></div>
  <div class="builder-about">
    <h3>Harbel Homes</h3>
    <p>A Harbel Homes é uma das maiores construtoras dos Estados Unidos, reconhecida pela qualidade, inovação e compromisso com o cliente em cada nova comunidade que entrega.</p>
  </div>
  <div class="stat" style="left:590px;top:40px"><b>40+</b><span>Cidades</span></div>
  <div class="stat" style="left:740px;top:40px"><b>18</b><span>Estados</span></div>
  <div class="stat" style="left:590px;top:190px"><span>Fundada</span><b style="font-size:22px">EM 1954</b></div>
  <div class="stat" style="left:740px;top:190px"><span>Mais de</span><b style="font-size:24px">600</b><span style="font-size:7px">Comunidades em<br>construção</span></div>
  <div class="img builder-photo" role="img" aria-label="Fachada de casa com varanda e jardim"></div>
</section>

<section class="lead">
  <div class="img branch" style="left:300px;top:200px;width:180px;height:50px" role="img" aria-label="Galho florido decorativo"></div>
  <div class="img branch" style="left:790px;top:200px;width:180px;height:50px;transform:scaleX(-1)" role="img" aria-label="Galho florido decorativo"></div>
  <div class="lead-circle">
    <small>Fale Com Nossa Equipe</small>
    <h2>No Que Voce Precisar</h2>
    <p>Responderemos em até um dia útil.</p>
    <div class="lead-row"><div class="f">Nome</div><div class="f">E-mail</div></div>
    <div class="lead-area">Mensagem</div>
    <span class="btn btn-orange">Enviar</span>
  </div>
  <div class="img skyline" role="img" aria-label="Silhueta suave de cidade"></div>
</section>

<footer class="site-footer">
  <div class="footer-col" style="left:240px;top:40px;width:220px">
    <h5><span class="pin"></span>São Paulo</h5>
    Av. Exemplo, 1200 – Sala 45<br>Vila Nova, São Paulo – SP
    <h5><span class="pin"></span>Orlando</h5>
    7800 Sample Blvd, Suite 210<br>Orlando, FL 32800
    <h5><span class="pin"></span>contato@coralparlor.com</h5>
  </div>
  <div class="footer-brand"><span class="dot"></span>CORAL PARLOR</div>
  <div class="footer-contacts">
    <span class="phone-pill">(11) 4000-0000</span><span class="phone-pill" style="background:var(--orange)">(407) 555-0100</span>
    <div class="footer-links">
      <span><i style="background:var(--pink)"></i>Fale com<br>Especialista</span>
      <span><i style="background:var(--teal)"></i>Agende sua<br>Consultoria</span>
    </div>
  </div>
  <div class="footer-bar">
    <span>© Coral Parlor – Todos os direitos reservados</span>
    <nav><span>Home</span><span>Sobre</span><span>Imóveis</span><span>Serviços</span><span>Contato</span></nav>
  </div>
</footer>

</body>
</html>
```